Steadway Halvicor

We're designing a website to sell Halvicor Supplements. Attached is an image of the words we want to say and general layout, but please use your best knowledge to make it better. This platform is intentionally simplistic because this is reaching an older demographic, so it should be very straightforward, attention-grabbing and extremely user-friendly, while still appearing reliable and professional.
Use your best judgement for color palate that conveys professional but approachable. Feel free to add imagery but don't overwhelm the page.
Updates
Designs look the same
Target Market(s)
65+ seniors
Number of Pages Required
1 page
Look and feel

```html
<!DOCTYPE html>
<html lang="en">
<head>
<meta charset="utf-8">
<title>Steadway Halvicor – Landing Page and Quote Dialog</title>
<link rel="stylesheet" href="https://fonts.googleapis.com/css2?family=Roboto:wght@400;500;700&family=Lato:wght@400;700&family=Nunito+Sans:wght@400;600&display=swap">
<style>
:root{
  --stage:#e0e0e0;
  --white:#ffffff;
  --ink:#111820;
  --muted:#4a4f57;
  --brand:#1a8db3;
  --blue:#1c5aa3;
  --blue-deep:#0c3b85;
  --red:#e8262c;
  --faq-bg:#eef2f9;
  --faq-line:#4f7fb8;
  --footer:#0f1c2a;
  --modal-head:#e6eef1;
}
*{box-sizing:border-box;margin:0;padding:0}
html,body{width:1089px;height:1200px;overflow:hidden;background:var(--stage)}
body{position:relative;font-family:"Roboto",Arial,sans-serif;color:var(--ink)}

.artboard{position:absolute;top:28px;width:487px;height:1144px;background:var(--white);overflow:hidden}
.artboard--page{left:34.5px}
.artboard--dialog{left:557.5px}

/* header */
.site-header{position:relative;height:33px;background:var(--white)}
.logo{position:absolute;left:19px;top:9px;font:500 12px/1 "Roboto",sans-serif;color:var(--brand);letter-spacing:.3px}
.main-nav{position:absolute;left:191px;top:12px;display:flex;gap:17px;font:400 7px/1 "Nunito Sans",sans-serif;color:#444}
.main-nav .is-active{color:var(--ink);position:relative}
.main-nav .is-active::after{content:"";position:absolute;left:5px;right:5px;bottom:-4px;height:1px;background:var(--blue)}

/* hero */
.hero{position:relative;height:238px;background:linear-gradient(90deg,#0b3a85 0%,#15489a 38%,#2a5d9e 52%,#7f9cc2 68%,#c8d5e4 100%);overflow:hidden}
.hero-photo{position:absolute;right:0;top:0;width:250px;height:238px;background:linear-gradient(110deg,rgba(40,85,150,0) 0%,rgba(150,175,205,.55) 30%,rgba(205,215,225,.7) 60%,rgba(225,230,236,.85) 100%)}
.hero-title{position:absolute;left:40px;top:56px;font:500 20.5px/1 "Roboto",sans-serif;color:var(--white)}
.hero-sub{position:absolute;left:41px;top:82px;font:400 10px/12.5px "Roboto",sans-serif;color:var(--white);width:200px}
.zip-form{position:absolute;display:flex;align-items:center;background:var(--white);border-radius:14px;padding:0 2px 0 9px}
.zip-form .pin{width:6px;height:8px;margin-right:4px;flex:none}
.zip-form .placeholder{flex:1;font:400 6.5px/1 "Roboto",sans-serif;color:#777}
.quote-btn{background:var(--red);color:var(--white);border-radius:12px;font:700 6.5px/1 "Roboto",sans-serif;display:flex;align-items:center;justify-content:center;letter-spacing:.2px}
.hero .zip-form{left:37.5px;top:116px;width:190px;height:23px}
.hero .quote-btn{width:68px;height:18px}
.hero-call{position:absolute;left:44px;top:151px;font:500 12.5px/1 "Roboto",sans-serif;color:var(--white);display:flex;align-items:center;gap:2px}
.hero-call svg{width:12px;height:12px}
.hero-note{position:absolute;left:45px;top:168px;font:400 7px/1 "Roboto",sans-serif;color:var(--white)}

/* section headings */
.section-title{font:500 13px/15px "Roboto",sans-serif;text-align:center;color:var(--ink)}
.section-rule{width:24px;height:1.5px;background:var(--blue);margin:6px auto 0}

/* benefits */
.benefits{position:relative;height:250px;background:var(--white)}
.benefits .section-title{position:absolute;left:0;right:0;top:25px}
.benefits .section-rule{position:absolute;left:231.5px;top:58px;margin:0}
.benefit{position:absolute;width:190px}
.benefit svg{position:absolute;left:0;top:0;width:36px;height:36px}
.benefit h3{position:absolute;left:48px;top:0;font:500 8.2px/10.5px "Roboto",sans-serif;color:var(--blue)}
.benefit p{position:absolute;left:48px;top:27px;width:122px;font:400 5.4px/8.8px "Roboto",sans-serif;color:#333}
.benefit--free{left:54px;top:76px}
.benefit--time{left:258px;top:76px}
.benefit--plan{left:54px;top:158px}
.benefit--expert{left:258px;top:158px}

/* faq */
.faq{position:relative;height:242px;background:var(--faq-bg)}
.faq .section-title{position:absolute;left:0;right:0;top:22px}
.faq .section-rule{position:absolute;left:231.5px;top:41px;margin:0}
.faq-item{position:absolute;left:89px;width:310px;border:1px solid var(--faq-line);background:var(--white);font-family:"Lato",sans-serif}
.faq-item h4{position:absolute;left:9px;top:7px;font:400 7px/1 "Lato",sans-serif;color:var(--ink)}
.faq-item .toggle{position:absolute;right:7px;top:6px;font:400 10px/1 "Lato",sans-serif;color:var(--blue)}
.faq-item p{position:absolute;left:9px;top:20px;width:292px;font:400 5.6px/7.3px "Lato",sans-serif;color:#333}
.faq-item--1{top:58px;height:22px}
.faq-item--2{top:84px;height:22px}
.faq-item--3{top:109px;height:45px}
.faq-item--4{top:157px;height:22px}
.faq-item--5{top:182px;height:23px}
.faq-item--4 h4,.faq-item--5 h4{font-size:6.6px}

/* articles */
.articles{position:relative;height:262px;background:linear-gradient(160deg,#1553bd 0%,#1a62d0 55%,#1b58c0 100%)}
.articles .section-title{position:absolute;left:0;right:0;top:27px;color:var(--white)}
.articles .section-rule{position:absolute;left:231.5px;top:58px;margin:0;background:var(--white)}
.article-card{position:absolute;top:68px;width:111px;height:152px;background:var(--white);border-radius:2px;box-shadow:0 2px 6px rgba(0,0,0,.2)}
.article-card--1{left:70px}.article-card--2{left:192px}.article-card--3{left:314px}
.article-photo{height:70px;margin:1px 1px 0;background:linear-gradient(135deg,#c9c2b0,#8f8f88)}
.article-card--2 .article-photo{background:linear-gradient(135deg,#eef0f2,#b9c3cc)}
.article-card--3 .article-photo{background:linear-gradient(135deg,#d7d9dc,#7c8590)}
.article-card h5{margin:13px 0 0 10px;font:400 6.3px/8.8px "Lato",sans-serif;color:var(--ink);text-transform:uppercase}
.article-card p{margin:5px 10px 0 10px;font:400 4.8px/7.7px "Lato",sans-serif;color:#555}
.article-card .more{display:block;margin:5px 0 0 11px;font:700 5.4px/1 "Lato",sans-serif;color:var(--red)}

/* quote band */
.quote-band{position:relative;height:55px;background:var(--white)}
.quote-band h2{position:absolute;left:69px;top:22px;font:500 12.3px/1 "Roboto",sans-serif;color:var(--ink)}
.quote-band .zip-form{left:240px;top:15px;width:198px;height:24px;border:1px solid #c9ccd1}
.quote-band .quote-btn{width:71px;height:18px}

/* footer */
.site-footer{position:relative;height:64px;background:var(--footer)}
.footer-nav{position:absolute;left:60px;top:22px;display:flex;gap:16px;font:400 6.6px/1 "Nunito Sans",sans-serif;color:var(--white)}
.footer-legal{position:absolute;left:60px;top:37px;font:400 5.3px/1 "Nunito Sans",sans-serif;color:var(--white)}
.social{position:absolute;left:372px;top:20px;display:flex;gap:3px}
.social span{width:14px;height:14px;border:1px solid var(--white);border-radius:50%}

/* dialog */
.overlay{position:absolute;inset:0;background:rgba(0,0,0,.62)}
.quote-dialog{position:absolute;left:87.5px;top:81.5px;width:320px;height:200px;background:var(--white);box-shadow:0 4px 14px rgba(0,0,0,.35)}
.dialog-head{height:42px;background:var(--modal-head);display:flex;align-items:center;justify-content:center;font:500 15.5px/1 "Roboto",sans-serif;color:#0d2d5e}
.dialog-close{position:absolute;right:8px;top:8px;width:11px;height:11px}
.dialog-divider{position:absolute;left:161px;top:52px;width:1px;height:137px;background:#d8dde2}
.dialog-or{position:absolute;left:153px;top:111px;width:16px;height:16px;border-radius:50%;background:#111;color:var(--white);font:700 5.5px/16px "Roboto",sans-serif;text-align:center}
.dialog-online{position:absolute;left:0;top:66px;width:168px;text-align:center}
.dialog-online h3{font:500 12.5px/1 "Roboto",sans-serif;color:var(--blue)}
.dialog-online p{margin:6px auto 0;width:118px;font:400 5.8px/7.7px "Roboto",sans-serif;color:var(--ink)}
.quote-dialog .zip-form{left:34.5px;top:108px;width:99px;height:22px;border:1px solid #9aa3ad}
.dialog-submit{position:absolute;left:35.5px;top:134.5px;width:98px;height:21px;border-radius:11px}
.dialog-phone{position:absolute;left:162px;top:66px;width:158px;text-align:center}
.dialog-phone svg{width:28px;height:36px}
.dialog-phone p{margin-top:4px;font:400 7.9px/11px "Roboto",sans-serif;color:var(--ink)}
.dialog-phone strong{display:block;margin-top:3px;font:500 11px/1 "Roboto",sans-serif;color:#0d2d5e}
</style>
</head>
<body>

<!-- Artboard 1: landing page -->
<main class="artboard artboard--page">
  <header class="site-header">
    <div class="logo">Steadway Halvicor</div>
    <nav class="main-nav"><span class="is-active">About</span><span>Our Quiz</span><span>Supplement Plan</span><span>Blog</span><span>Why Us</span><span>Contact</span></nav>
  </header>

  <section class="hero">
    <div class="hero-photo" role="img" aria-label="Photo of a smiling senior woman with glasses sitting at a laptop"></div>
    <h1 class="hero-title">Steadway Halvicor</h1>
    <p class="hero-sub">Be confident in choosing the Halvicor Supplement plan that’s right for you.</p>
    <div class="zip-form">
      <svg class="pin" viewBox="0 0 12 16"><path d="M6 0a6 6 0 0 0-6 6c0 4.5 6 10 6 10s6-5.5 6-10a6 6 0 0 0-6-6zm0 8.5A2.5 2.5 0 1 1 6 3.5a2.5 2.5 0 0 1 0 5z" fill="#8a9098"/></svg>
      <span class="placeholder">Enter Zip Code</span>
      <span class="quote-btn">Get Free Quote</span>
    </div>
    <div class="hero-call">
      <svg viewBox="0 0 24 24"><path d="M6.6 2.5l3 3.5-1.8 2.3a13 13 0 0 0 7.9 7.9l2.3-1.8 3.5 3-2 2.6C12 19.4 4.6 12 3.9 4.5z" fill="none" stroke="#fff" stroke-width="1.4"/></svg>
      Call (800) 555-0142
    </div>
    <p class="hero-note">And talk to a live agent to help you find the right plan!</p>
  </section>

  <section class="benefits">
    <h2 class="section-title">Understanding The Benefits of<br>Halvicor Insurance</h2>
    <div class="section-rule"></div>
    <div class="benefit benefit--free">
      <svg viewBox="0 0 36 36" fill="none" stroke="#1c3f78" stroke-width="1.4"><circle cx="18" cy="18" r="14"/><path d="M21.5 13.5c-.8-1.2-2-1.8-3.5-1.8-2 0-3.4 1-3.4 2.6 0 3.6 7.2 2 7.2 5.8 0 1.7-1.6 2.8-3.8 2.8-1.7 0-3-.7-3.8-2M18 9.5v17"/></svg>
      <h3>Steadway Halvicor is<br>Free to Use</h3>
      <p>Lorem ipsum dolor sit amet consectetuer adipiscing elit Nam cursus Morbi ut mi Nullam enim leo egestas id condimentum at laoreet</p>
    </div>
    <div class="benefit benefit--time">
      <svg viewBox="0 0 36 36" fill="none" stroke="#1c3f78" stroke-width="1.4"><circle cx="18" cy="18" r="14"/><circle cx="18" cy="18" r="10.5"/><path d="M18 11v7l5 3"/></svg>
      <h3>It Helps You to<br>Save Time</h3>
      <p>Lorem ipsum dolor sit amet consectetuer adipiscing elit Nam cursus Morbi ut mi Nullam enim leo egestas id condimentum at laoreet</p>
    </div>
    <div class="benefit benefit--plan">
      <svg viewBox="0 0 36 36" fill="none" stroke="#1c3f78" stroke-width="1.4"><rect x="6" y="5" width="22" height="28" rx="1.5"/><rect x="12" y="3" width="10" height="4" rx="1"/><circle cx="11" cy="14" r="1.5"/><circle cx="11" cy="20" r="1.5"/><circle cx="11" cy="26" r="1.5"/><path d="M15 14h9M15 20h9M15 26h9M31 10v20"/></svg>
      <h3>Plan<br>Recommendation</h3>
      <p>Lorem ipsum dolor sit amet consectetuer adipiscing elit Nam cursus Morbi ut mi Nullam enim leo egestas id condimentum at laoreet</p>
    </div>
    <div class="benefit benefit--expert">
      <svg viewBox="0 0 36 36" fill="none" stroke="#1c3f78" stroke-width="1.4"><path d="M7 20v-4a11 11 0 0 1 22 0v4"/><rect x="4" y="18" width="5" height="9" rx="2"/><rect x="27" y="18" width="5" height="9" rx="2"/><path d="M30 27c0 4-4 5-9 5"/><rect x="17" y="30" width="5" height="3.5" rx="1.5"/></svg>
      <h3>Talk to a U.S. based,<br>licensed expert</h3>
      <p>Lorem ipsum dolor sit amet consectetuer adipiscing elit Nam cursus Morbi ut mi Nullam enim leo egestas id condimentum at laoreet</p>
    </div>
  </section>

  <section class="faq">
    <h2 class="section-title">Frequently Asked Questions</h2>
    <div class="section-rule"></div>
    <div class="faq-item faq-item--1"><h4>Nunc tempus felis vitae urna Vivamus porttitor ?</h4><span class="toggle">+</span></div>
    <div class="faq-item faq-item--2"><h4>Phasellus pellentesque aliquam enim Proin dui lectus cursus?</h4><span class="toggle">+</span></div>
    <div class="faq-item faq-item--3"><h4>Morbi eget arcu Morbi porta libero ?</h4><span class="toggle">–</span><p>Pellentesque faucibus Ut accumsan ultricies elit Maecenas at justo id velit placerat molestie Donec dictum lectus non odio Cras a ante vitae enim iaculis aliquam Mauris nunc quam venenatis nec</p></div>
    <div class="faq-item faq-item--4"><h4>Fusce tellus Sed metus augue convallis et vehicula?</h4><span class="toggle">+</span></div>
    <div class="faq-item faq-item--5"><h4>Nunc tempus felis vitae urna Vivamus porttitor neque ?</h4><span class="toggle">+</span></div>
  </section>

  <section class="articles">
    <h2 class="section-title">Recently Written By Our<br>Insurance Experts</h2>
    <div class="section-rule"></div>
    <article class="article-card article-card--1"><div class="article-photo" role="img" aria-label="Photo of a senior woman reviewing paperwork at home"></div><h5>Sed ut perspiciatis unde<br>omnis iste natus</h5><p>Sed ut perspiciatis unde omnis iste natus error sit voluptatem accusntium dolor-emque laudantium, totam</p><span class="more">Learn More ›</span></article>
    <article class="article-card article-card--2"><div class="article-photo" role="img" aria-label="Photo of a doctor writing on a clipboard"></div><h5>Sed ut perspiciatis unde<br>omnis iste natus</h5><p>Sed ut perspiciatis unde omnis iste natus error sit voluptatem accusntium dolor-emque laudantium, totam</p><span class="more">Learn More ›</span></article>
    <article class="article-card article-card--3"><div class="article-photo" role="img" aria-label="Photo of a doctor talking with a patient"></div><h5>Sed ut perspiciatis unde<br>omnis iste natus</h5><p>Sed ut perspiciatis unde omnis iste natus error sit voluptatem accusntium dolor-emque laudantium, totam</p><span class="more">Learn More ›</span></article>
  </section>

  <section class="quote-band">
    <h2>Get a Free Halvicor Quote</h2>
    <div class="zip-form">
      <svg class="pin" viewBox="0 0 12 16"><path d="M6 0a6 6 0 0 0-6 6c0 4.5 6 10 6 10s6-5.5 6-10a6 6 0 0 0-6-6zm0 8.5A2.5 2.5 0 1 1 6 3.5a2.5 2.5 0 0 1 0 5z" fill="#8a9098"/></svg>
      <span class="placeholder">Enter Zip Code</span>
      <span class="quote-btn">Get Free Quote</span>
    </div>
  </section>

  <footer class="site-footer">
    <nav class="footer-nav"><span>About</span><span>Our Quiz</span><span>Supplement Plan</span><span>Blog</span><span>Why Us</span><span>Contact</span></nav>
    <p class="footer-legal">© 2020 Company Name | All Rights Reserved | Disclaimer</p>
    <div class="social"><span></span><span></span><span></span><span></span></div>
  </footer>
</main>

<!-- Artboard 2: landing page with quote dialog open -->
<main class="artboard artboard--dialog">
  <header class="site-header">
    <div class="logo">Steadway Halvicor</div>
    <nav class="main-nav"><span class="is-active">About</span><span>Our Quiz</span><span>Supplement Plan</span><span>Blog</span><span>Why Us</span><span>Contact</span></nav>
  </header>

  <section class="hero">
    <div class="hero-photo" role="img" aria-label="Photo of a smiling senior woman with glasses sitting at a laptop"></div>
    <h1 class="hero-title">Steadway Halvicor</h1>
    <p class="hero-sub">Be confident in choosing the Halvicor Supplement plan that’s right for you.</p>
    <div class="zip-form">
      <svg class="pin" viewBox="0 0 12 16"><path d="M6 0a6 6 0 0 0-6 6c0 4.5 6 10 6 10s6-5.5 6-10a6 6 0 0 0-6-6zm0 8.5A2.5 2.5 0 1 1 6 3.5a2.5 2.5 0 0 1 0 5z" fill="#8a9098"/></svg>
      <span class="placeholder">Enter Zip Code</span>
      <span class="quote-btn">Get Free Quote</span>
    </div>
    <div class="hero-call">
      <svg viewBox="0 0 24 24"><path d="M6.6 2.5l3 3.5-1.8 2.3a13 13 0 0 0 7.9 7.9l2.3-1.8 3.5 3-2 2.6C12 19.4 4.6 12 3.9 4.5z" fill="none" stroke="#fff" stroke-width="1.4"/></svg>
      Call (800) 555-0142
    </div>
    <p class="hero-note">And talk to a live agent to help you find the right plan!</p>
  </section>

  <section class="benefits">
    <h2 class="section-title">Understanding The Benefits of<br>Halvicor Insurance</h2>
    <div class="section-rule"></div>
    <div class="benefit benefit--free">
      <svg viewBox="0 0 36 36" fill="none" stroke="#1c3f78" stroke-width="1.4"><circle cx="18" cy="18" r="14"/><path d="M21.5 13.5c-.8-1.2-2-1.8-3.5-1.8-2 0-3.4 1-3.4 2.6 0 3.6 7.2 2 7.2 5.8 0 1.7-1.6 2.8-3.8 2.8-1.7 0-3-.7-3.8-2M18 9.5v17"/></svg>
      <h3>Steadway Halvicor is<br>Free to Use</h3>
      <p>Lorem ipsum dolor sit amet consectetuer adipiscing elit Nam cursus Morbi ut mi Nullam enim leo egestas id condimentum at laoreet</p>
    </div>
    <div class="benefit benefit--time">
      <svg viewBox="0 0 36 36" fill="none" stroke="#1c3f78" stroke-width="1.4"><circle cx="18" cy="18" r="14"/><circle cx="18" cy="18" r="10.5"/><path d="M18 11v7l5 3"/></svg>
      <h3>It Helps You to<br>Save Time</h3>
      <p>Lorem ipsum dolor sit amet consectetuer adipiscing elit Nam cursus Morbi ut mi Nullam enim leo egestas id condimentum at laoreet</p>
    </div>
    <div class="benefit benefit--plan">
      <svg viewBox="0 0 36 36" fill="none" stroke="#1c3f78" stroke-width="1.4"><rect x="6" y="5" width="22" height="28" rx="1.5"/><rect x="12" y="3" width="10" height="4" rx="1"/><circle cx="11" cy="14" r="1.5"/><circle cx="11" cy="20" r="1.5"/><circle cx="11" cy="26" r="1.5"/><path d="M15 14h9M15 20h9M15 26h9M31 10v20"/></svg>
      <h3>Plan<br>Recommendation</h3>
      <p>Lorem ipsum dolor sit amet consectetuer adipiscing elit Nam cursus Morbi ut mi Nullam enim leo egestas id condimentum at laoreet</p>
    </div>
    <div class="benefit benefit--expert">
      <svg viewBox="0 0 36 36" fill="none" stroke="#1c3f78" stroke-width="1.4"><path d="M7 20v-4a11 11 0 0 1 22 0v4"/><rect x="4" y="18" width="5" height="9" rx="2"/><rect x="27" y="18" width="5" height="9" rx="2"/><path d="M30 27c0 4-4 5-9 5"/><rect x="17" y="30" width="5" height="3.5" rx="1.5"/></svg>
      <h3>Talk to a U.S. based,<br>licensed expert</h3>
      <p>Lorem ipsum dolor sit amet consectetuer adipiscing elit Nam cursus Morbi ut mi Nullam enim leo egestas id condimentum at laoreet</p>
    </div>
  </section>

  <section class="faq">
    <h2 class="section-title">Frequently Asked Questions</h2>
    <div class="section-rule"></div>
    <div class="faq-item faq-item--1"><h4>Nunc tempus felis vitae urna Vivamus porttitor ?</h4><span class="toggle">+</span></div>
    <div class="faq-item faq-item--2"><h4>Phasellus pellentesque aliquam enim Proin dui lectus cursus?</h4><span class="toggle">+</span></div>
    <div class="faq-item faq-item--3"><h4>Morbi eget arcu Morbi porta libero ?</h4><span class="toggle">–</span><p>Pellentesque faucibus Ut accumsan ultricies elit Maecenas at justo id velit placerat molestie Donec dictum lectus non odio Cras a ante vitae enim iaculis aliquam Mauris nunc quam venenatis nec</p></div>
    <div class="faq-item faq-item--4"><h4>Fusce tellus Sed metus augue convallis et vehicula?</h4><span class="toggle">+</span></div>
    <div class="faq-item faq-item--5"><h4>Nunc tempus felis vitae urna Vivamus porttitor neque ?</h4><span class="toggle">+</span></div>
  </section>

  <section class="articles">
    <h2 class="section-title">Recently Written By Our<br>Insurance Experts</h2>
    <div class="section-rule"></div>
    <article class="article-card article-card--1"><div class="article-photo" role="img" aria-label="Photo of a senior woman reviewing paperwork at home"></div><h5>Sed ut perspiciatis unde<br>omnis iste natus</h5><p>Sed ut perspiciatis unde omnis iste natus error sit voluptatem accusntium dolor-emque laudantium, totam</p><span class="more">Learn More ›</span></article>
    <article class="article-card article-card--2"><div class="article-photo" role="img" aria-label="Photo of a doctor writing on a clipboard"></div><h5>Sed ut perspiciatis unde<br>omnis iste natus</h5><p>Sed ut perspiciatis unde omnis iste natus error sit voluptatem accusntium dolor-emque laudantium, totam</p><span class="more">Learn More ›</span></article>
    <article class="article-card article-card--3"><div class="article-photo" role="img" aria-label="Photo of a doctor talking with a patient"></div><h5>Sed ut perspiciatis unde<br>omnis iste natus</h5><p>Sed ut perspiciatis unde omnis iste natus error sit voluptatem accusntium dolor-emque laudantium, totam</p><span class="more">Learn More ›</span></article>
  </section>

  <section class="quote-band">
    <h2>Get a Free Halvicor Quote</h2>
    <div class="zip-form">
      <svg class="pin" viewBox="0 0 12 16"><path d="M6 0a6 6 0 0 0-6 6c0 4.5 6 10 6 10s6-5.5 6-10a6 6 0 0 0-6-6zm0 8.5A2.5 2.5 0 1 1 6 3.5a2.5 2.5 0 0 1 0 5z" fill="#8a9098"/></svg>
      <span class="placeholder">Enter Zip Code</span>
      <span class="quote-btn">Get Free Quote</span>
    </div>
  </section>

  <footer class="site-footer">
    <nav class="footer-nav"><span>About</span><span>Our Quiz</span><span>Supplement Plan</span><span>Blog</span><span>Why Us</span><span>Contact</span></nav>
    <p class="footer-legal">© 2020 Company Name | All Rights Reserved | Disclaimer</p>
    <div class="social"><span></span><span></span><span></span><span></span></div>
  </footer>

  <div class="overlay"></div>

  <div class="quote-dialog" role="dialog" aria-label="Steadway Halvicor Quote">
    <div class="dialog-head">Steadway Halvicor Quote</div>
    <svg class="dialog-close" viewBox="0 0 12 12"><path d="M1 1l10 10M11 1L1 11" stroke="#222" stroke-width="1"/></svg>
    <div class="dialog-online">
      <h3>Online</h3>
      <p>Lorem ipsum dolor sit amet consectetuer adipiscing elit Nam cursus</p>
    </div>
    <div class="zip-form">
      <svg class="pin" viewBox="0 0 12 16"><path d="M6 0a6 6 0 0 0-6 6c0 4.5 6 10 6 10s6-5.5 6-10a6 6 0 0 0-6-6zm0 8.5A2.5 2.5 0 1 1 6 3.5a2.5 2.5 0 0 1 0 5z" fill="#8a9098"/></svg>
      <span class="placeholder">Enter Zip Code</span>
    </div>
    <span class="quote-btn dialog-submit">Get Free Quote</span>
    <div class="dialog-divider"></div>
    <div class="dialog-or">OR</div>
    <div class="dialog-phone">
      <svg viewBox="0 0 28 36" fill="none" stroke="#e8262c" stroke-width="1.3"><path d="M4 18v-4a10 10 0 0 1 20 0v4"/><rect x="2" y="15" width="5" height="10" rx="2"/><rect x="21" y="15" width="5" height="10" rx="2"/><path d="M23.5 25c0 4-4 6-8.5 6"/><rect x="11" y="29.5" width="5" height="3.5" rx="1.5"/></svg>
      <p>And talk to a live agent to help<br>you find the right plan!</p>
      <strong>Call (800) 555-0142</strong>
    </div>
  </div>
</main>

</body>
</html>
```